PLEASE READ - DESIGN for Music Cover Tunevault - DJ and Female Singer

A nice cover to be put on Tunevault.
Definitely will be on Tunevault and All Media
Name of the song: Marivella
Singer name: Tara Wolskind
DJ name: DJ Roland Kestry

Marivella definition: A desire to be in the Sun

We need eye catching icon or something that can attract people's eyes when they see it immediately. Design must be elegant. This is not some type of Club Banging Music. The singer is a romantic and sophisticated audiophile jazz acoustic recording artist. DJ is not playing in some clubs but exclusive.

Photo of singer and DJ can be on the cover OR just photo of the singer OR just an Icon wifh their names and the song name.

Avoid these colors: Pink, Purple, Silver !!
For the background color try: A mixed of Black or Gold with Elegant Yellow, Pastel Orange, or light Blue.
For name of the song and Icon color : can be of Gold or even Red or White.
Or you can try and mix it all up yourself

Icon ideas: can be a combination of letter Capital C with small B & Capital V alone or mixed with a sun logo or half of Sun. Some cool stuff.
CB is Tara Wolskind
V is for the DJ name

Target Market(s)

Young Adult, Lounge Crowd, Club Goers / Lounge Goers, Ladies, Executives, Adults, Music Industry

Industry/Entity Type

Entertainment Industry

Font styles to use
Serif

Requirements
Must have
• MARIVELLA ( song name )
• Available on Tunevault logo
• EYE CATCHING ICON or LOGO
Should not have
• Avoid this color :
• Pink, Purple, Silver, White
• Our first project was already consisting these colors, we will attach the old design of the first song but PLEASE DO NOT apply the older design to this new project :)

```html
<!DOCTYPE html>
<html lang="en">
<head>
<meta charset="utf-8">
<title>Marivella – DJ Roland Kestry &amp; Tara Wolskind</title>
<link rel="stylesheet" href="https://fonts.googleapis.com/css2?family=Poiret+One&family=Questrial&display=swap">
<style>
  :root {
    --ink-deep: #160a07;
    --ember: #8f2a14;
    --flame: #d8642a;
    --amber: #f0a04a;
    --glow: #f5e4c4;
    --haze: #dfe4cf;
    --cream: #f6ecd6;
    --accent-orange: #f7931e;
    --badge-black: #111111;
    --badge-edge: #8a8a8a;
  }
  * { margin: 0; padding: 0; box-sizing: border-box; }
  html, body {
    width: 1200px;
    height: 1200px;
    overflow: hidden;
    background: var(--ink-deep);
  }
  .cover {
    position: relative;
    width: 1200px;
    height: 1200px;
    overflow: hidden;
    font-family: "Questrial", Arial, sans-serif;
  }
  .cover__backdrop {
    position: absolute;
    inset: 0;
    background:
      radial-gradient(circle at 30% 80%, rgba(252, 240, 210, 0.85) 0, rgba(252, 240, 210, 0) 220px),
      radial-gradient(circle at 560px 500px,
        var(--ink-deep) 0,
        #2a100a 150px,
        var(--ember) 300px,
        var(--flame) 420px,
        var(--amber) 540px,
        var(--glow) 700px,
        var(--haze) 880px);
  }
  .cover__emblem {
    position: absolute;
    left: 440px;
    top: 385px;
    width: 290px;
    height: 120px;
    display: flex;
    align-items: center;
    justify-content: center;
    gap: 18px;
  }
  .emblem__sun {
    width: 58px;
    height: 58px;
    border-radius: 50%;
    background: var(--accent-orange);
    flex: none;
  }
  .emblem__name {
    font-family: "Poiret One", Georgia, serif;
    font-size: 62px;
    line-height: 1;
    letter-spacing: 2px;
    color: var(--cream);
  }
  .cover__title {
    position: absolute;
    left: 0;
    top: 500px;
    width: 1200px;
    height: 180px;
  }
  .cover__title text {
    font-family: "Poiret One", Georgia, serif;
    font-size: 128px;
  }
  .title__letter { fill: var(--cream); }
  .title__letter--accent { fill: var(--accent-orange); }
  .cover__credits {
    position: absolute;
    left: 0;
    right: 0;
    top: 663px;
    text-align: center;
    color: var(--cream);
    font-size: 29px;
    letter-spacing: 1.5px;
    line-height: 41px;
    text-transform: uppercase;
  }
  .store-badge {
    position: absolute;
    left: 957px;
    top: 1096px;
    width: 151px;
    height: 54px;
    border-radius: 8px;
    background: var(--badge-black);
    border: 1px solid var(--badge-edge);
    color: #ffffff;
    display: flex;
    align-items: center;
    gap: 10px;
    padding-left: 14px;
  }
  .store-badge__dot {
    width: 22px;
    height: 22px;
    border-radius: 50%;
    background: #ffffff;
    flex: none;
  }
  .store-badge__text { display: flex; flex-direction: column; line-height: 1; }
  .store-badge__lead { font-size: 11px; margin-bottom: 4px; }
  .store-badge__name { font-size: 21px; }
</style>
</head>
<body>
  <main class="cover">
    <div class="cover__backdrop" role="img" aria-label="Abstract radial blur in warm black, red, orange and cream tones swirling around the centre"></div>

    <div class="cover__emblem">
      <span class="emblem__name">Solwyn</span>
      <span class="emblem__sun"></span>
    </div>

    <svg class="cover__title" viewBox="0 500 1200 180" aria-label="Marivella">
      <text x="182" y="640" textLength="848" lengthAdjust="spacing">
        <tspan class="title__letter title__letter--accent">M</tspan><tspan class="title__letter">ARIVELL</tspan><tspan class="title__letter title__letter--accent">A</tspan>
      </text>
      <line x1="180" y1="654" x2="1032" y2="654" stroke="var(--accent-orange)" stroke-width="5"/>
    </svg>

    <div class="cover__credits">
      <p class="credits__dj">DJ Roland Kestry</p>
      <p class="credits__singer">Tara Wolskind</p>
    </div>

    <div class="store-badge">
      <span class="store-badge__dot"></span>
      <span class="store-badge__text">
        <span class="store-badge__lead">Get it on</span>
        <span class="store-badge__name">Tunevault</span>
      </span>
    </div>
  </main>
</body>
</html>
```